This is a laser engraving business. I’m looking for a business card that includes a minimalist laser logo/design with the company name Brisk Harbor Crafts and telephone number 654-210-3378 and email briskharborcrafts@mailrove.com

Industry/Entity Type

Laser engraving

Contact Information for Business Card

Laser logo/design that represents laser engraving

```html
<!DOCTYPE html>
<html lang="en">
<head>
<meta charset="utf-8">
<title>Brisk Harbor Crafts – Business Card</title>
<link rel="stylesheet" href="https://fonts.googleapis.com/css2?family=Saira+Semi+Condensed:wght@700&family=Poppins:wght@400;500&display=swap">
<style>
  :root {
    --bg: #1e1e1f;
    --card: #1a1a1b;
    --card-edge: #2a2a2b;
    --white: #f4f4f4;
    --gloss: #3a3a3c;
    --red: #e0262b;
  }
  html, body {
    margin: 0;
    width: 1200px;
    height: 1200px;
    overflow: hidden;
    background: var(--bg);
  }
  .canvas {
    position: relative;
    width: 1200px;
    height: 1200px;
    display: flex;
    flex-direction: column;
    align-items: center;
    justify-content: center;
    gap: 60px;
  }
  .card {
    position: relative;
    width: 860px;
    height: 491px;
    background: var(--card);
    border: 1px solid var(--card-edge);
    border-radius: 22px;
    box-shadow: 0 18px 40px rgba(0,0,0,0.45);
    box-sizing: border-box;
  }
  .brand-lockup {
    display: flex;
    flex-direction: column;
    align-items: center;
    gap: 8px;
  }
  .brand-name {
    font-family: "Saira Semi Condensed", sans-serif;
    font-weight: 700;
    font-size: 40px;
    letter-spacing: 1px;
    text-transform: uppercase;
    line-height: 1;
    display: flex;
    align-items: center;
    gap: 12px;
    white-space: nowrap;
  }
  .brand-dot {
    width: 14px;
    height: 14px;
    border-radius: 50%;
    flex: none;
  }
  .brand-tagline {
    font-family: "Poppins", sans-serif;
    font-weight: 500;
    font-size: 15px;
    letter-spacing: 4px;
    text-transform: uppercase;
    line-height: 1;
    white-space: nowrap;
  }
  /* back side */
  .card-back { display: flex; align-items: center; justify-content: center; }
  .card-back .brand-name, .card-back .brand-tagline { color: var(--gloss); }
  .card-back .brand-dot { background: var(--gloss); }
  /* front side */
  .card-front .brand-block {
    position: absolute;
    left: 30px;
    top: 0;
    bottom: 0;
    width: 400px;
    display: flex;
    align-items: center;
    justify-content: center;
  }
  .card-front .brand-name { color: var(--white); font-size: 28px; }
  .card-front .brand-dot { background: var(--red); width: 12px; height: 12px; }
  .card-front .brand-tagline { color: var(--white); font-size: 12px; letter-spacing: 3px; }
  .divider {
    position: absolute;
    left: 450px;
    top: 100px;
    width: 2px;
    height: 290px;
    background: var(--white);
  }
  .contact-list {
    position: absolute;
    left: 435px;
    top: 198px;
    margin: 0;
    padding: 0;
    list-style: none;
    font-family: "Poppins", sans-serif;
    font-size: 20px;
    color: var(--white);
  }
  .contact-item {
    display: flex;
    align-items: center;
    gap: 20px;
    height: 46px;
    white-space: nowrap;
  }
  .contact-icon {
    width: 32px;
    height: 32px;
    flex: none;
  }
</style>
</head>
<body>
<main class="canvas">
  <section class="card card-back" aria-label="Card back">
    <div class="brand-lockup">
      <div class="brand-name"><span class="brand-dot"></span>Brisk Harbor Crafts</div>
      <div class="brand-tagline">Laser Engraving</div>
    </div>
  </section>

  <section class="card card-front" aria-label="Card front">
    <div class="brand-block">
      <div class="brand-lockup">
        <div class="brand-name"><span class="brand-dot"></span>Brisk Harbor Crafts</div>
        <div class="brand-tagline">Laser Engraving</div>
      </div>
    </div>
    <div class="divider"></div>
    <ul class="contact-list">
      <li class="contact-item">
        <svg class="contact-icon" viewBox="0 0 32 32" aria-hidden="true">
          <circle cx="16" cy="16" r="14" fill="#1a1a1b" stroke="#f4f4f4" stroke-width="2"/>
          <path d="M11 9.5l3 0 1.2 3.4-1.8 1.3a9 9 0 0 0 4.4 4.4l1.3-1.8 3.4 1.2v3a1.5 1.5 0 0 1-1.6 1.5C14.7 22 10 17.3 9.5 11.1A1.5 1.5 0 0 1 11 9.5z" fill="#e0262b"/>
        </svg>
        <span>654-210-3378</span>
      </li>
      <li class="contact-item">
        <svg class="contact-icon" viewBox="0 0 32 32" aria-hidden="true">
          <circle cx="16" cy="16" r="14" fill="#1a1a1b" stroke="#f4f4f4" stroke-width="2"/>
          <rect x="9" y="11" width="14" height="10" rx="1" fill="#e0262b"/>
          <path d="M9.5 11.5l6.5 5 6.5-5" fill="none" stroke="#1a1a1b" stroke-width="1.4"/>
        </svg>
        <span>briskharborcrafts@mailrove.com</span>
      </li>
    </ul>
  </section>
</main>
</body>
</html>
```